Swimming Pool Service Website needed!!!

Hi Everyone! Thanks for looking at my contest. I PROMISE to provide excellent feedback during this process.

I am starting a new swimming pool business cleaning company in San Diego, California and would like your help in making it similar to one of these two websites that are already functioning.

http://www.brightlagoonworks.example/services-repair.html

http://tidemarkaquacare.example/commercial-pool-cleaning.php

I like these two because they are easy to read, classy, sophisticated and have nice pictures of really clean & clear pools.

I really like the blue on white color format.

I do not have a logo, but the name of my company is GLIMMERWAVE POOL SERVICE.

My tag line is: Water so pure, it sparkles like a summer sky. (does not need to have the quotes around "in"...maybe just italics for this word IN?) You decide for me.

I would like to have a logo designed that incorporates some sort of easy to read letters. I do not want cursive (handwriting) letters. I thought about having a "reflection" of letters (mirror image), but think that this will be hard to read from far away. Maybe you can surprise me and come up with an idea that works using the a mirror image....but I'm not sure. I was leaning toward plain old BLOCK letters as I think it would be easy to read on my truck.

I would like to have 5 pages on my website:
1) Home
2) About Us (Know Your Poolman) / Why Hire Us
3) Services Offered
4) FAQ's
5) Contact

I am looking for a fully-functioning website (coded). Upon selection of the design winner, I am offering to increase the budget/payment by $100-$125 for the coding of all the pages. So anyone looking at participating in this contest, should be willing and able to provide the coding to the webpages that i've requested.

Target Market(s)

Upper middle-class homeowners who have a pool

Industry/Entity Type

Pool Service

Number of Pages Required

5+ page

Font styles to use
Serif

Colors
0455a3
3276b5
85acd3
85cae6
ffffff
33a6d7
0592cd

Requirements
Must have
• The Home page must have this picture highlighted in the top of the page:
• http://www.mesawaterpro.example/
• Must have pictures of some high-end pools. Any that you can find on the internet are wonderful.
• Must have a table on the right of the home page that mentions the service areas that we go to:
• • Carmel Valley (92130)
• • Del Mar (92014)
• • Rancho Santa Fe (92067)
• • Solana Beach (92075)
• • Santaluz (92127)
• • Cardiff (92007)
• • Encinitas (92024)
• • Carlsbad (92009, 92008)
• • La Jolla (92037)
• • Pacific Beach (92109)
• • Mira Mesa (92126)
• • Sorrento Valley (92121)
• • Clairemont (92117)
• • Rancho Bernardo (92127, 92128)
• • Rancho Penasquitos (92129)
• • Poway (92064)
• •
Nice to have
• Maybe incorporate some pictures of some kids (or families) playing in pools on the Why Hire Us page?
• I also like the feel of this website, but posting this page just for reference so you can get a feel more of what I like:
• http://www.crestlinepool.example/
• I like the FAQ's page from this website. I like how you can click on the question and then it pops up with the answer. http://www.dunewoodpoolcare.example/pool-spa-fountain-faqs/

```html
<!DOCTYPE html>
<html lang="en">
<head>
<meta charset="utf-8">
<title>Glimmerwave Pool Service</title>
<link href="https://fonts.googleapis.com/css2?family=Lato:ital,wght@0,300;0,400;0,700;1,400&family=Tinos:ital,wght@0,700;1,700&display=swap" rel="stylesheet">
<style>
:root{
  --blue:#33a6d7;
  --blue-deep:#0455a3;
  --blue-mid:#3276b5;
  --blue-soft:#85cae6;
  --topbar:#a3a3a3;
  --text:#8a8a8a;
  --text-dark:#555;
  --dark:#2e2e2e;
  --dark-services:#25282e;
  --white:#fff;
  --rule:#dcdcdc;
}
*{margin:0;padding:0;box-sizing:border-box}
html,body{width:1200px;height:2604px;overflow:hidden}
body{position:relative;font-family:"Lato",Arial,sans-serif;color:var(--text);background:var(--white)}
ul{list-style:none}
h1,h2,h3,h4{font-weight:400}
.abs{position:absolute}

/* top bar */
.topbar{left:0;top:0;width:1200px;height:35px;background:var(--topbar);color:var(--white);font-size:11px}
.topbar .phone{left:184px;top:11px;display:flex;align-items:center;gap:7px}
.topbar .social{right:183px;top:13px;display:flex;gap:21px}
.topbar .social span{width:8px;height:8px;border-radius:50%;background:var(--white);display:block}

/* header */
.header{left:0;top:35px;width:1200px;height:75px;background:var(--white)}
.brand{left:184px;top:18px;font-weight:700;font-size:34px;letter-spacing:1px;color:var(--blue);line-height:1}
.nav{left:470px;top:19px;display:flex;align-items:center}
.nav a{font-size:12.5px;color:var(--blue);text-decoration:none;display:block}
.nav .active{background:var(--blue);color:var(--white);padding:10px 15px;border-radius:2px;margin-right:30px}
.nav a+a{margin-right:42px}

/* hero */
.hero{left:0;top:110px;width:1200px;height:550px;
  background:linear-gradient(180deg,#d6e7ee 0%,#a9d3e7 40%,#4fb0de 70%,#2a90cf 100%)}
.hero-caption{left:377px;top:218px;width:479px;height:93px;background:rgba(255,255,255,.38);text-align:center}
.hero-title{font-family:"Tinos",Georgia,serif;font-style:italic;font-weight:700;font-size:25px;color:#5e5e5e;margin-top:22px;letter-spacing:.5px;text-shadow:1px 1px 1px rgba(255,255,255,.6)}
.hero-tag{font-family:"Tinos",Georgia,serif;font-style:italic;font-weight:700;font-size:17px;color:var(--blue-deep);margin-top:4px}
.hero-dots{left:583px;top:522px;display:flex;gap:4px}
.hero-dots span{width:10px;height:10px;border-radius:50%;background:var(--white);display:block}
.hero-dots span:first-child{background:transparent;border:2px solid var(--white)}

/* section title */
.section-title{display:flex;align-items:center;justify-content:center;gap:10px;font-size:22px;font-weight:400;color:var(--blue);letter-spacing:.5px;white-space:nowrap}
.section-title.on-dark{color:var(--white)}

/* mission */
.mission-title{left:0;top:703px;width:1200px}
.mission-photo{left:184px;top:756px;width:404px;height:206px;background:linear-gradient(180deg,#4db7e3,#1f94d2 60%,#1a7fc0);border-radius:2px}
.mission-text{left:612px;top:752px;width:405px;font-size:10.6px;line-height:19.6px;color:var(--text);text-align:justify}
.mission-text p+p{margin-top:20px}

/* services */
.services{left:0;top:1014px;width:1200px;height:726px;background:linear-gradient(180deg,#2a2c31 0%,#26282d 40%,#2d3542 75%,#1e2430 100%);color:var(--white)}
.services-title{left:0;top:38px;width:1200px}
.col-head{font-size:17px;font-weight:400;color:var(--white)}
.sub-head{font-size:14px;font-weight:400;color:var(--white)}
.ticks li{position:relative;padding-left:20px;font-size:10.3px;line-height:21.8px;color:var(--white)}
.ticks li::before{content:"›";position:absolute;left:0;top:6px;width:10px;height:10px;border-radius:50%;background:var(--white);color:var(--dark-services);font-size:10px;line-height:9px;text-align:center;font-weight:700}
.res-col{left:184px;top:96px;width:400px}
.res-col .sub-head{margin-top:26px;margin-bottom:14px}
.res-col .sub-head.second{margin-top:31px;margin-bottom:15px}
.com-col{left:612px;top:96px;width:420px}
.com-col .col-head{margin-bottom:13px}
.areas-title{left:544px;top:566px;font-size:17px;font-weight:400;color:var(--white)}
.areas{left:184px;top:612px;width:850px;display:grid;grid-template-columns:212px 216px 212px 210px}
.areas .ticks li{line-height:18.5px;font-size:10.6px}
.areas .ticks li::before{top:4px}

/* faq / testimonials */
.faq-title{left:184px;top:1785px;width:404px}
.testi-title{left:612px;top:1785px;width:405px}
.faq{left:184px;top:1845px;width:404px}
.faq-q{display:flex;justify-content:space-between;align-items:center;font-size:11.3px;color:var(--text-dark);padding-bottom:7px;border-bottom:1px solid var(--rule)}
.faq-q .plus{width:22px;height:22px;background:var(--blue);color:var(--white);font-size:17px;line-height:22px;text-align:center}
.faq-a{font-size:10.3px;line-height:18.4px;color:var(--text);text-align:justify;padding:8px 0 14px}
.faq-q+.faq-q{margin-top:10px}
.avatar{left:754px;top:1850px;width:118px;height:118px;border-radius:50%;background:radial-gradient(circle at 50% 45%,#c9a58f,#8a5a45 55%,#3a2a26)}
.quote-mark{left:778px;top:1982px;width:70px;text-align:center;font-family:"Tinos",Georgia,serif;font-weight:700;font-size:52px;line-height:1;color:#9a9a9a}
.testi-text{left:612px;top:2028px;width:405px;text-align:center;font-size:10.8px;line-height:18px;color:var(--text-dark)}
.testi-dots{left:797px;top:2074px;display:flex;gap:6px}
.testi-dots span{width:9px;height:9px;border-radius:50%;background:var(--blue);display:block}
.testi-dots span:first-child{background:transparent;border:2px solid var(--blue)}

/* footer */
.footer{left:0;top:2135px;width:1200px;height:469px;background:var(--dark);color:var(--white)}
.foot-head{font-size:18px;font-weight:400;color:var(--white);letter-spacing:.3px}
.foot-head::after{content:"";display:block;width:36px;height:2px;background:var(--white);margin-top:13px}
.keep{left:184px;top:30px;width:410px}
.keep p{font-size:10.3px;line-height:17.5px;color:#e3e3e3;margin-top:14px}
.contact-item{display:flex;align-items:flex-start;gap:14px;font-size:11.3px;line-height:17px;color:#e8e8e8}
.icon-ring{width:40px;height:40px;border-radius:50%;border:1.5px solid var(--white);display:flex;align-items:center;justify-content:center;flex:none}
.email-item{left:184px;top:154px}
.phone-item{left:399px;top:154px}
.addr-item{left:184px;top:224px}
.ring-row{left:184px;top:310px;display:flex;gap:10px}
.ring-row span{width:38px;height:38px;border-radius:50%;border:1px solid #9a9a9a;display:block}
.form{left:612px;top:86px;width:260px}
.field{font-size:10px;color:#8d8d8d;padding:6px 6px 8px;border-bottom:1px solid #5a5a5a}
.field+.field{margin-top:10px}
.field.area{height:90px;border:1px solid #5a5a5a;margin-top:14px}
.send{margin-top:14px;width:70px;height:30px;border:1.5px solid var(--white);border-radius:2px;font-size:11px;text-align:center;line-height:27px;color:var(--white);letter-spacing:.5px}
.links{left:896px;top:30px;width:121px}
.links ul{margin-top:14px}
.links li{position:relative;padding-left:18px;font-size:10.3px;line-height:28px;color:#e8e8e8;border-bottom:1px solid #4a4a4a}
.links li::before{content:"›";position:absolute;left:0;top:9px;width:10px;height:10px;border-radius:50%;background:var(--white);color:var(--dark);font-size:10px;line-height:9px;text-align:center;font-weight:700}
.copy-rule{left:184px;top:413px;width:833px;height:1px;background:#444}
.copyright{left:0;top:433px;width:1200px;text-align:center;font-size:9.5px;color:#6d6d6d}
</style>
</head>
<body>

<div class="abs topbar">
  <div class="abs phone">
    <svg width="10" height="10" viewBox="0 0 24 24"><path fill="#fff" d="M6.6 10.8a15 15 0 0 0 6.6 6.6l2.2-2.2c.3-.3.7-.4 1-.2 1.1.4 2.3.6 3.6.6.6 0 1 .4 1 1V20c0 .6-.4 1-1 1A17 17 0 0 1 3 4c0-.6.4-1 1-1h3.5c.6 0 1 .4 1 1 0 1.3.2 2.5.6 3.6.1.3 0 .7-.2 1z"/></svg>
    <span>(858) 555-0142</span>
  </div>
  <div class="abs social" aria-label="Social links"><span></span><span></span><span></span></div>
</div>

<header class="abs header">
  <div class="abs brand">GLIMMERWAVE</div>
  <nav class="abs nav">
    <a class="active">Home</a>
    <a>About Us</a>
    <a>Services Offered</a>
    <a>FAQ's</a>
    <a>Why Hire Us</a>
    <a>Contact</a>
  </nav>
</header>

<section class="abs hero" role="img" aria-label="Photo of a resort pool with clear blue water, cabanas and palm trees">
  <div class="abs hero-caption">
    <div class="hero-title">GLIMMERWAVE POOL SERVICE</div>
    <div class="hero-tag">Water so pure, it sparkles like a summer sky.</div>
  </div>
  <div class="abs hero-dots"><span></span><span></span><span></span></div>
</section>

<h2 class="abs section-title mission-title">
  <svg width="46" height="10"><line x1="0" y1="5" x2="36" y2="5" stroke="#33a6d7" stroke-width="1.5"/><circle cx="41" cy="5" r="4" fill="none" stroke="#33a6d7" stroke-width="1.5"/></svg>
  OUR MISSION
  <svg width="46" height="10"><circle cx="5" cy="5" r="4" fill="none" stroke="#33a6d7" stroke-width="1.5"/><line x1="10" y1="5" x2="46" y2="5" stroke="#33a6d7" stroke-width="1.5"/></svg>
</h2>
<div class="abs mission-photo" role="img" aria-label="Photo of three children in swim goggles smiling in a blue pool"></div>
<div class="abs mission-text">
  <p>At Glimmerwave Pool Service, we understand that your pool is an important investment. Whether it's part of your business or in your backyard, it needs to be well taken care of to ensure its longevity and your peace of mind. At Glimmerwave Pool Service, we pride ourselves in setting the standard in our industry. What sets us apart from our competition is our commitment to excellence. Our exceptional service and competitive price make us the clear choice for your pool service needs.</p>
  <p>Glimmerwave Pool Service has been providing spectacular pool &amp; spa cleaning and maintenance service for over 7 years. Our technicians are professionally trained and are committed to providing outstanding customer service through our honest, hands-on approach. From our timely response system to our flexible program offerings, Glimmerwave Pool Service understands the importance of servicing your every need.</p>
</div>

<section class="abs services" role="img" aria-label="Dim evening photo of a pool deck with lounge chairs, used as a dark backdrop">
  <h2 class="abs section-title on-dark services-title">
    <svg width="46" height="10"><line x1="0" y1="5" x2="36" y2="5" stroke="#fff" stroke-width="1.5"/><circle cx="41" cy="5" r="4" fill="none" stroke="#fff" stroke-width="1.5"/></svg>
    OUR SERVICES
    <svg width="46" height="10"><circle cx="5" cy="5" r="4" fill="none" stroke="#fff" stroke-width="1.5"/><line x1="10" y1="5" x2="46" y2="5" stroke="#fff" stroke-width="1.5"/></svg>
  </h2>

  <div class="abs res-col">
    <h3 class="col-head">Residential Services</h3>
    <h4 class="sub-head">Weekly Pool and Spa Service</h4>
    <ul class="ticks">
      <li>Once per week service on a consistent day</li>
      <li>Net Out Floating Debris</li>
      <li>Clean Tiles/Waterline</li>
      <li>Vacuum Pool and Spa as Needed</li>
      <li>Brush Steps and Walls</li>
      <li>Empty Skimmer and Pump Strainer Baskets</li>
      <li>Check Chemicals and Adjust Accordingly</li>
      <li>Examine Pool Equipment Communicate to homeowner regarding any issues</li>
      <li>Backwash Filter as needed and Recharge with DE</li>
    </ul>
    <h4 class="sub-head second">Additional Residential Services</h4>
    <ul class="ticks">
      <li>Equipment Repair and Installation</li>
      <li>Algae Treatment</li>
      <li>Acid Washes</li>
      <li>Equipment Inspection for new home buyers</li>
    </ul>
  </div>

  <div class="abs com-col">
    <h3 class="col-head">Commercial Services</h3>
    <ul class="ticks">
      <li>Licensed and Bonded Technicians</li>
      <li>Health Department Certified</li>
      <li>CPO (Certified Pool Operator)</li>
      <li>Insured for your peace of mind</li>
      <li>Pool Vacuuming and Cleaning</li>
      <li>Scheduled weekly or monthly pool cleaning</li>
      <li>Water Chemistry Testing and Balancing</li>
      <li>Written Logs of Visits and Water Chemistry</li>
      <li>Pool Brushing and Skimming</li>
      <li>Cleaning of Tiles and Water Lines</li>
      <li>Maintain Pool decking and furniture</li>
      <li>Leak Detection and Repair</li>
      <li>Pool Openings and Closings</li>
      <li>Maintaining proper water levels</li>
      <li>Work with County Health Departments for all inspections and visits.</li>
      <li>Maintenance of all pumps, filters, cleaners, heaters, chlorinators,<br>flow meters, pressure gauges, etc.</li>
    </ul>
  </div>

  <h3 class="abs areas-title">Service Areas:</h3>
  <div class="abs areas">
    <ul class="ticks"><li>Carmel Valley (92130)</li><li>Del Mar (92014)</li><li>Rancho Santa Fe (92067)</li><li>Solana Beach (92075)</li></ul>
    <ul class="ticks"><li>Santaluz (92127)</li><li>Cardiff (92007)</li><li>Encinitas (92024)</li><li>Carlsbad (92009, 92008)</li></ul>
    <ul class="ticks"><li>La Jolla (92037)</li><li>Pacific Beach (92109)</li><li>Mira Mesa (92126)</li><li>Sorrento Valley (92121)</li></ul>
    <ul class="ticks"><li>Clairemont (92117)</li><li>Rancho Bernardo (92127, 92128)</li><li>Rancho Penasquitos (92129)</li><li>Poway (92064)</li></ul>
  </div>
</section>

<h2 class="abs section-title faq-title">
  <svg width="46" height="10"><line x1="0" y1="5" x2="36" y2="5" stroke="#33a6d7" stroke-width="1.5"/><circle cx="41" cy="5" r="4" fill="none" stroke="#33a6d7" stroke-width="1.5"/></svg>
  FAQ
  <svg width="46" height="10"><circle cx="5" cy="5" r="4" fill="none" stroke="#33a6d7" stroke-width="1.5"/><line x1="10" y1="5" x2="46" y2="5" stroke="#33a6d7" stroke-width="1.5"/></svg>
</h2>
<h2 class="abs section-title testi-title">
  <svg width="46" height="10"><line x1="0" y1="5" x2="36" y2="5" stroke="#33a6d7" stroke-width="1.5"/><circle cx="41" cy="5" r="4" fill="none" stroke="#33a6d7" stroke-width="1.5"/></svg>
  TESTIMONIALS
  <svg width="46" height="10"><circle cx="5" cy="5" r="4" fill="none" stroke="#33a6d7" stroke-width="1.5"/><line x1="10" y1="5" x2="46" y2="5" stroke="#33a6d7" stroke-width="1.5"/></svg>
</h2>

<div class="abs faq">
  <div class="faq-q"><span>Why do my pool and spa need to be chlorinated?</span><span class="plus">+</span></div>
  <div class="faq-a">Pools should be disinfected continuously by a chemical which imparts a residual effect. Chlorine is a type of "disinfectant", also called a "sanitizer". Disinfects or sanitizers destroy living microorganisms and bacteria, preventing the transmission of disease. There are several types of disinfectants, such as chlorine, bromine, salt chlorination, ozone, and UV light. Pools need a disinfectant with a measurable residual.</div>
  <div class="faq-q"><span>Why do my pool and spa need to be chlorinated?</span><span class="plus">+</span></div>
  <div class="faq-q"><span>Why do my pool and spa need to be chlorinated?</span><span class="plus">+</span></div>
  <div class="faq-q"><span>Why do my pool and spa need to be chlorinated?</span><span class="plus">+</span></div>
</div>

<div class="abs avatar" role="img" aria-label="Round portrait photo of a happy customer"></div>
<div class="abs quote-mark">&ldquo;</div>
<p class="abs testi-text">Glimmerwave is as honest as they come.&nbsp; I am very happy with their<br>service and know-how, and my pool has never looked better.</p>
<div class="abs testi-dots"><span></span><span></span><span></span></div>

<footer class="abs footer">
  <div class="abs keep">
    <h3 class="foot-head">KEEP IN TOUCH</h3>
    <p>Lorem ipsum dolor sit amet consectetur mauris magna, lacinia ac purus quis, rutrum bibendum leo. Nullam sit amet nibh eu odio ornare laoreet dolor imperdiet est ut tristique auctor sed.</p>
  </div>
  <div class="abs contact-item email-item">
    <span class="icon-ring"><svg width="14" height="11" viewBox="0 0 14 11"><rect x=".75" y=".75" width="12.5" height="9.5" fill="none" stroke="#fff" stroke-width="1.3"/><polyline points="1,1 7,6 13,1" fill="none" stroke="#fff" stroke-width="1.3"/></svg></span>
    <span>Email:<br>hello@glimmerwave.example</span>
  </div>
  <div class="abs contact-item phone-item">
    <span class="icon-ring"><svg width="15" height="15" viewBox="0 0 24 24"><path fill="#fff" d="M6.6 10.8a15 15 0 0 0 6.6 6.6l2.2-2.2c.3-.3.7-.4 1-.2 1.1.4 2.3.6 3.6.6.6 0 1 .4 1 1V20c0 .6-.4 1-1 1A17 17 0 0 1 3 4c0-.6.4-1 1-1h3.5c.6 0 1 .4 1 1 0 1.3.2 2.5.6 3.6.1.3 0 .7-.2 1z"/></svg></span>
    <span>Phone:<br>(858) 555-0142</span>
  </div>
  <div class="abs contact-item addr-item">
    <span class="icon-ring"><svg width="12" height="16" viewBox="0 0 12 16"><path fill="#fff" d="M6 0a6 6 0 0 0-6 6c0 4.5 6 10 6 10s6-5.5 6-10a6 6 0 0 0-6-6zm0 8.3A2.3 2.3 0 1 1 6 3.7a2.3 2.3 0 0 1 0 4.6z"/></svg></span>
    <span>123 Some Street, New York, US<br>PO BOX: 44 455<br>Flat 28, 3rd floor</span>
  </div>
  <div class="abs ring-row" aria-label="Social links"><span></span><span></span><span></span><span></span><span></span><span></span><span></span></div>

  <form class="abs form">
    <div class="field">Enter Your Name</div>
    <div class="field">Enter Your Email Address</div>
    <div class="field">Your Phone Number</div>
    <div class="field area">Your Message</div>
    <div class="send">SEND</div>
  </form>

  <div class="abs links">
    <h3 class="foot-head">QUICK LINKS</h3>
    <ul>
      <li>Services Offered</li>
      <li>Know Your Poolman</li>
      <li>Our Mission</li>
      <li>Residential Services</li>
      <li>Why You Need Us</li>
      <li>Service Areas</li>
      <li>Contact Us</li>
      <li>Commercial Services</li>
      <li>Contact Us</li>
    </ul>
  </div>

  <div class="abs copy-rule"></div>
  <p class="abs copyright">© Copyright 2015 GLIMMERWAVE POOL SERVICE. All Rights Reserved.</p>
</footer>

</body>
</html>
```